I'm an Executive Coach. I need a cover for a leadership book.

Title: Quiet Compass Wide Horizon Guidance from the Center of the Spirit. The focus in my work "Soul Woven Purpose" I use a lot of fire and heart-centered frame work and imagery. The book should have a leadership presence with an inspirational feel. The purpose is to invite really smart leaders to pay attention and to lead from their heart so they can have great impact in the work they do and the lives they live. priyalangford.example to see site branding, colors. Author: Priya Langford

Target Market(s)

The audience is those lead others from the manager level to the executive level and entrepreneurs starting and leading their own companies They are usually trailblazers, care about connecting with people as they lead. The big message is being confifent to lead ftom values, intention and from what matters most.

Industry/Entity Type

Executive coaching

Font styles to use
Serif

Requirements
Must have
• Lighter feel. Perhaps avoid a total black background.
Nice to have
• While it is a leadership book, i would like it to feel creative and inviting not authoritative.
Should not have
• Dark colors as the main color

```html
<!DOCTYPE html>
<html lang="en">
<head>
<meta charset="utf-8">
<title>Quiet Compass Wide Horizon — Priya Langford</title>
<link href="https://fonts.googleapis.com/css2?family=Marcellus+SC&family=Parisienne&family=Josefin+Sans:wght@300&display=swap" rel="stylesheet">
<style>
  :root {
    --sky-top: #5ff6fd;
    --sky-bottom: #2fe6ea;
    --title-white: #ffffff;
    --title-shade: rgba(40, 80, 90, 0.55);
    --ember: #e8552e;
    --ember-soft: #f28a4a;
    --glow: #fffbe6;
  }
  * { margin: 0; padding: 0; box-sizing: border-box; }
  html, body { width: 840px; height: 1200px; overflow: hidden; }
  body { background: var(--sky-bottom); }

  .cover {
    position: relative;
    width: 840px;
    height: 1200px;
    overflow: hidden;
    background: linear-gradient(180deg, var(--sky-top) 0%, #55f3fb 45%, var(--sky-bottom) 100%);
  }

  .title {
    position: absolute;
    left: 0; right: 0; top: 0;
    text-align: center;
    font-family: "Marcellus SC", serif;
    color: var(--title-white);
    text-shadow: 1px 1px 0 var(--title-shade), 2px 2px 3px rgba(30, 70, 80, 0.35);
    font-weight: 400;
  }
  .title__line {
    position: absolute;
    left: 0; right: 0;
    white-space: nowrap;
    line-height: 1;
  }
  .title__line--1 { top: 66px;  font-size: 78px; }
  .title__line--2 { top: 138px; font-size: 78px; }
  .title__line--3 { top: 214px; font-size: 78px; }
  .title__line--4 { top: 292px; font-size: 62px; letter-spacing: 1px; }

  .title__script {
    position: absolute;
    left: 0; right: 0;
    top: 346px;
    text-align: center;
    font-family: "Parisienne", cursive;
    font-size: 92px;
    line-height: 1;
    color: var(--ember);
    text-shadow: none;
  }

  .cover-art {
    position: absolute;
    left: 150px;
    top: 440px;
    width: 540px;
    height: 540px;
    border-radius: 50%;
    background:
      radial-gradient(circle at 30% 32%, var(--glow) 0%, rgba(255, 245, 200, 0.8) 10%, rgba(255, 255, 255, 0) 30%),
      radial-gradient(ellipse at 52% 62%, var(--ember-soft) 0%, var(--ember) 35%, rgba(232, 85, 46, 0.35) 55%, rgba(95, 246, 253, 0) 70%);
  }

  .author {
    position: absolute;
    left: 0; right: 0;
    top: 1116px;
    text-align: center;
    font-family: "Josefin Sans", sans-serif;
    font-weight: 300;
    font-size: 40px;
    letter-spacing: 7px;
    color: var(--ember);
    line-height: 1;
  }
</style>
</head>
<body>
  <main class="cover">
    <h1 class="title">
      <span class="title__line title__line--1">Quiet Compass</span>
      <span class="title__line title__line--2">Wide Horizon</span>
      <span class="title__line title__line--3">Guidance</span>
      <span class="title__line title__line--4">from the Center</span>
      <span class="title__script">of the Spirit</span>
    </h1>

    <div class="cover-art" role="img" aria-label="Illustration of a glowing orange heart made of scattered cubes, with a bright sunburst at its upper left"></div>

    <p class="author">PRIYA LANGFORD</p>
  </main>
</body>
</html>
```